Business Card Design for Orthopaedic Surgeon

This is a double-sided glossy business card. I prefer baby blue, teal, and green as color schemes. I have my logo already (many colors that you can choose from). I have photos and examples of my old card (very bland but has the information in it). I also have one that my assistant tried to design, but the writing is too small and I don't love the formatting. But it is close!
I would like my logo to be on the business card but I'm uploading my logo in many different colors so you can choose which one looks best based on the color scheme. I also uploaded many sized headshots so you can choose the best resolution one.

Additional information:
Correct business address:
4382 NW 58th Lane, Suite 305
Tamarac, FL 33417

Everything else on both business cards are accurate.

I actually need 2 different business cards generated. One that includes my cell phone number-- Personal cell: 585-314-9062 in addition to Office phone: (954) 316-4870 and Office Fax: 954-316-4881. Again, one card would have my personal cell and one wouldn't

Overall I just think the baby blue card (uploaded) is missing something on the front--of course it is also missing my office phone/fax/personal cell. I do want my website on the front too. Email: info@wellsorthocare.example

You can use your discretion about what goes on the front vs. what goes on the back to eliminated clutter.

Oh and on the back, I would like to list "Conditions Treated" (not specialties include). The list is:
Carpal Tunnel
Trigger Finger
Ganglion Cysts
Hand Tumors
Han & Wrist Arthritis
Hand, Wrist & Elbow Tendonitis
Fractures of the Hand, Wrist, Elbow and Humerus
Nerve Injuries of the Hand, Wrist & Elbow
Microsurgery
Wrist Arthroscopy
Endoscopic Surgery

Target Market(s)

Primary care doctors, Lawyers, patients

Industry/Entity Type

Medical

Contact Information for Business Card

Please see above in project description

Colors

Designer to choose colors to be used in the design.

Requirements
Must have
• -Correct office info, Board Certified Orthopaedic Hand & Upper Extremity Surgeon
Nice to have
• Something that is classy and wow!

```html
<!DOCTYPE html>
<html lang="en">
<head>
<meta charset="utf-8">
<title>Wells Hand – Business Card</title>
<link href="https://fonts.googleapis.com/css2?family=Tenor+Sans&display=swap" rel="stylesheet">
<style>
  :root {
    --bg: #e9e7e4;
    --card-black: #161818;
    --card-black-soft: #2a2c2d;
    --white: #ffffff;
    --teal: #17a89a;
    --green: #2fd38a;
    --blue: #2f5fae;
    --violet: #5b62b8;
    --gold: #d2b07a;
    --text-light: #f2f2f2;
  }
  * { box-sizing: border-box; margin: 0; padding: 0; }
  html, body { width: 1200px; height: 913px; overflow: hidden; }
  body {
    background: var(--bg);
    font-family: "Tenor Sans", "Optima", sans-serif;
    position: relative;
  }
  .card {
    position: absolute;
    left: 240px;
    width: 720px;
    height: 411px;
    border-radius: 4px;
    overflow: hidden;
    box-shadow: 0 10px 30px rgba(0,0,0,.25);
    background: linear-gradient(135deg, var(--card-black-soft), var(--card-black) 60%);
  }
  .card--back { top: 30px; }
  .card--front { top: 472px; }
  .card-art { position: absolute; inset: 0; }

  .brand {
    position: absolute;
    display: flex;
    align-items: center;
    gap: 10px;
    color: var(--gold);
    font-size: 24px;
    letter-spacing: 4px;
    text-transform: uppercase;
    white-space: nowrap;
  }
  .brand__dot {
    width: 18px; height: 18px;
    border-radius: 50%;
    background: var(--gold);
  }
  .card--back .brand { top: 52px; right: 60px; }
  .card--front .brand { top: 40px; right: 58px; font-size: 22px; }

  .conditions {
    position: absolute;
    left: 44px;
    top: 44px;
  }
  .conditions__title {
    color: var(--green);
    font-size: 24px;
    font-weight: 400;
    letter-spacing: 1px;
    text-transform: uppercase;
    margin-bottom: 12px;
  }
  .conditions__list { list-style: none; }
  .conditions__item {
    display: flex;
    align-items: center;
    gap: 12px;
    color: var(--teal);
    font-size: 16px;
    line-height: 25px;
  }
  .conditions__item::before {
    content: "";
    width: 14px; height: 2px;
    background: linear-gradient(90deg, var(--blue), var(--teal));
  }

  .photo {
    position: absolute;
    left: 92px; top: 102px;
    width: 206px; height: 206px;
    border-radius: 50%;
    border: 4px solid var(--teal);
    background: radial-gradient(circle at 50% 40%, #c9a58a 0%, #5a3a2c 45%, #1b1b1e 80%);
  }

  .identity {
    position: absolute;
    right: 40px;
    top: 96px;
    text-align: right;
    white-space: nowrap;
  }
  .identity__name {
    color: var(--teal);
    font-size: 25px;
    font-weight: 400;
    letter-spacing: 1px;
    text-transform: uppercase;
  }
  .identity__title {
    color: var(--text-light);
    font-size: 14px;
    line-height: 19px;
    margin-top: 4px;
  }

  .contact-list {
    position: absolute;
    list-style: none;
    color: var(--text-light);
    font-size: 13px;
    white-space: nowrap;
  }
  .contact-list--phones { right: 40px; top: 178px; }
  .contact-list--web { left: 404px; top: 246px; }
  .contact {
    display: flex;
    align-items: center;
    gap: 8px;
    line-height: 22px;
  }
  .contact-list--phones .contact { justify-content: flex-end; }
  .icon { width: 14px; height: 14px; flex: none; }
  .icon path, .icon rect, .icon circle { fill: none; stroke: var(--teal); stroke-width: 1.6; }
  .icon .solid { fill: var(--teal); stroke: none; }

  .rule {
    position: absolute;
    left: 404px; right: 30px; top: 300px;
    height: 1px;
    background: linear-gradient(90deg, var(--teal), var(--blue));
  }
  .address {
    position: absolute;
    left: 404px; right: 30px; top: 312px;
    display: flex;
    align-items: center;
    justify-content: space-between;
    gap: 6px;
    color: var(--text-light);
    font-size: 11px;
    white-space: nowrap;
  }
</style>
</head>
<body>

<section class="card card--back" aria-label="Card back">
  <div class="brand"><span class="brand__dot"></span>Wells Hand</div>
  <div class="conditions">
    <h2 class="conditions__title">Conditions Treated</h2>
    <ul class="conditions__list">
      <li class="conditions__item">Carpal Tunnel</li>
      <li class="conditions__item">Trigger Finger</li>
      <li class="conditions__item">Ganglion Cysts</li>
      <li class="conditions__item">Hand Tumors</li>
      <li class="conditions__item">Han &amp; Wrist Arthritis</li>
      <li class="conditions__item">Hand, Wrist &amp; Elbow Tendonitis</li>
      <li class="conditions__item">Fractures of the Hand, Wrist, Elbow and Humerus</li>
      <li class="conditions__item">Nerve Injuries of the Hand, Wrist &amp; Elbow</li>
      <li class="conditions__item">Microsurgery</li>
      <li class="conditions__item">Wrist Arthroscopy</li>
      <li class="conditions__item">Endoscopic Surgery</li>
    </ul>
  </div>
</section>

<section class="card card--front" aria-label="Card front">
  <svg class="card-art" width="720" height="411" viewBox="0 0 720 411" aria-hidden="true">
    <defs>
      <linearGradient id="band" x1="0" y1="0" x2="0" y2="1">
        <stop offset="0" stop-color="#1b7fa8"/>
        <stop offset=".3" stop-color="#17b0a0"/>
        <stop offset=".7" stop-color="#17b0a0"/>
        <stop offset="1" stop-color="#2a5fae"/>
      </linearGradient>
      <linearGradient id="edge" x1="0" y1="0" x2="0" y2="1">
        <stop offset="0" stop-color="#1a8fb0"/>
        <stop offset="1" stop-color="#5b62b8"/>
      </linearGradient>
    </defs>
    <polygon points="0,0 40,0 0,200" fill="#050607"/>
    <polygon points="40,0 330,0 392,411 0,411 0,200" fill="#ffffff"/>
    <polygon points="40,0 52,0 10,200 0,250 0,200" fill="url(#edge)"/>
    <rect x="165" y="0" width="60" height="411" fill="url(#band)"/>
    <polygon points="330,0 342,0 404,411 392,411" fill="url(#edge)"/>
  </svg>

  <div class="photo" role="img" aria-label="Headshot portrait of the surgeon"></div>

  <div class="brand"><span class="brand__dot"></span>Wells Hand</div>

  <div class="identity">
    <h1 class="identity__name">Renata Wells, MD</h1>
    <p class="identity__title">Board Certified Orthopaedic<br>Hand &amp; Upper Extremity Surgeon</p>
  </div>

  <ul class="contact-list contact-list--phones">
    <li class="contact">585-314-9062<svg class="icon" viewBox="0 0 14 14"><rect x="4" y="1" width="6" height="12" rx="1"/></svg></li>
    <li class="contact">(954) 316-4870<svg class="icon" viewBox="0 0 14 14"><path class="solid" d="M2 5c0-2 10-2 10 0v1H9V4.5H5V6H2zM3 7h8l1 5H2z"/></svg></li>
    <li class="contact">954-316-4881<svg class="icon" viewBox="0 0 14 14"><rect x="2" y="5" width="10" height="7"/><path d="M4 5V1.5h6V5M4 9h6"/></svg></li>
  </ul>

  <ul class="contact-list contact-list--web">
    <li class="contact">info@wellsorthocare.example<svg class="icon" viewBox="0 0 14 14"><rect x="1.5" y="3" width="11" height="8"/><path d="M1.5 3 7 8l5.5-5"/></svg></li>
    <li class="contact">www.wellsorthocare.example<svg class="icon" viewBox="0 0 14 14"><circle cx="7" cy="7" r="5.5"/><path d="M1.5 7h11M7 1.5c3 3 3 8 0 11M7 1.5c-3 3-3 8 0 11"/></svg></li>
  </ul>

  <div class="rule"></div>
  <p class="address"><span>4382 NW 58th Lane, Suite 305, Tamarac, FL 33417</span>
    <svg class="icon" viewBox="0 0 14 14"><path class="solid" d="M7 13S2.5 8 2.5 5.5a4.5 4.5 0 0 1 9 0C11.5 8 7 13 7 13zm0-6a1.6 1.6 0 1 0 0-3.2A1.6 1.6 0 0 0 7 7z"/></svg>
  </p>
</section>

</body>
</html>
```